Corvane Link Marketing Website

Corvane Link is the brand for a series of nation-wide internet peering exchanges operated by the Tallowmere Network Society Inc. (TNSI), a not-for-profit association founded in 1995.

Our current website is built on Drupal, and we are looking to migrate to WordPress with a similarly clean and modern theme:

http://www.corvanelink.example/

Target Market(s)

Technical and professional staff from the telecommunications industry in Australia.

Industry/Entity Type

Telecom

Font styles to use
Sans Serif

Requirements
Must have
• Responsive layout for mobile viewers
• Compatible with WordPress 4.2.2 and PHP 5.5.
• Winning entry will provide a completed WordPress theme file compatible .
• Usage of the "Corvane Link" logo must comply with the attached style guide.

```html
<!DOCTYPE html>
<html lang="en">
<head>
<meta charset="utf-8">
<title>Corvane Link — Carrier neutral internet peering</title>
<link rel="stylesheet" href="https://fonts.googleapis.com/css2?family=Open+Sans:wght@300;400;600;700&display=swap">
<style>
:root{
  --blue:#3a7bc8;
  --orange:#f08a24;
  --lime:#9cc63b;
  --teal:#19b5b0;
  --magenta:#e3387f;
  --red:#e2432e;
  --yellow:#f2b41c;
  --ink:#333;
  --muted:#888;
  --band:#f1f1f1;
  --footer:#2e2e2e;
  --footer-text:#9a9a9a;
}
*{box-sizing:border-box;margin:0;padding:0}
html,body{width:741px;height:1200px;overflow:hidden;background:#fff}
body{font-family:"Open Sans",Arial,sans-serif;color:var(--ink);position:relative}

.site-header{position:absolute;left:0;top:0;width:741px;height:69px;background:#fff}
.brand{position:absolute;left:70px;top:8px;height:52px;padding:0 14px;display:flex;align-items:center;gap:9px;background:#fff;box-shadow:0 1px 4px rgba(0,0,0,.15)}
.brand-mark{width:16px;height:16px;background:var(--blue)}
.brand-name{font-weight:700;font-size:16px;color:var(--blue);letter-spacing:.3px}
.main-nav{position:absolute;left:346px;top:0;display:flex}
.nav-tile{width:51.5px;height:54px;display:flex;flex-direction:column;align-items:center;justify-content:center;gap:6px;color:#fff;font-size:6.5px;font-weight:600;text-transform:uppercase}
.nav-tile svg{width:16px;height:16px}

.hero{position:absolute;left:0;top:69px;width:741px;height:289px;background:linear-gradient(135deg,#3c3c3c 0%,#5d5d5d 40%,#2b2b2b 100%)}
.hero-arrow{position:absolute;top:135px;width:14px;height:20px;background:rgba(0,0,0,.45);display:flex;align-items:center;justify-content:center}
.hero-title{position:absolute;left:210px;top:108px;font-size:46px;font-weight:300;color:var(--orange);line-height:1}
.hero-text{position:absolute;left:210px;top:164px;width:270px;font-size:12px;line-height:17px;color:#fff}

.intro{position:absolute;left:0;top:376px;width:741px;text-align:center}
.intro h2{font-size:17px;font-weight:600;letter-spacing:1px}
.intro p{width:400px;margin:12px auto 0;font-size:9.5px;line-height:14px;color:var(--muted)}

.services{position:absolute;left:0;top:482px;width:741px;height:234px;background:var(--band);text-align:center}
.services h2{padding-top:18px;font-size:22px;font-weight:600;letter-spacing:1px}
.cards{position:absolute;left:91px;top:66px;display:flex;gap:44px}
.card{width:149px;height:136px;color:#fff;padding:14px 12px 0}
.card svg{width:20px;height:20px}
.card h3{margin-top:8px;font-size:8px;font-weight:700;letter-spacing:.4px}
.card p{margin-top:10px;font-size:7px;line-height:10px;opacity:.9}
.card-blue{background:var(--blue)}.card-orange{background:var(--orange)}.card-yellow{background:var(--yellow)}

.features{position:absolute;left:0;top:716px;width:741px;height:210px;background:linear-gradient(90deg,#fff 0%,#f3f3f3 60%,#fff 100%)}
.feature-photo{position:absolute;left:136px;top:18px;width:210px;height:170px;background:linear-gradient(135deg,#2d2f33,#6b8fa8 55%,#9fb04a)}
.feature-list{position:absolute;left:365px;top:56px;list-style:none;font-size:8.5px;line-height:13px;color:var(--muted);text-transform:uppercase}
.feature-list li::before{content:"› ";color:var(--orange)}
.btn-join{position:absolute;left:365px;top:150px;padding:4px 10px;background:var(--yellow);color:#fff;font-size:7px;font-weight:700}

.partners{position:absolute;left:0;top:936px;width:741px;text-align:center}
.partners h2{font-size:13px;font-weight:600;letter-spacing:.5px}
.partner-row{display:flex;justify-content:center;gap:34px;margin-top:60px;align-items:center}
.partner{font-size:15px;font-weight:600;color:#555}

.site-footer{position:absolute;left:0;top:1119px;width:741px;height:81px;background:var(--footer);color:var(--footer-text);font-size:7px}
.footer-nav{position:absolute;left:70px;top:14px;display:flex;gap:18px;text-transform:uppercase}
.footer-contact{position:absolute;left:70px;top:40px}
.footer-copy{position:absolute;left:70px;top:60px}
.footer-social{position:absolute;right:70px;top:14px;text-align:right}
.social-row{display:flex;gap:4px;margin-top:6px}
.social-row span{width:12px;height:12px;background:#555}
</style>
</head>
<body>
<header class="site-header">
  <div class="brand"><span class="brand-mark"></span><span class="brand-name">Corvane Link</span></div>
  <nav class="main-nav">
    <div class="nav-tile" style="background:var(--blue)"><svg viewBox="0 0 16 16"><path d="M2 3h12v8H7l-3 3v-3H2z" fill="none" stroke="#fff" stroke-width="1.4"/></svg>Home</div>
    <div class="nav-tile" style="background:var(--orange)"><svg viewBox="0 0 16 16"><circle cx="8" cy="8" r="5.5" fill="none" stroke="#fff" stroke-width="1.4"/></svg>About</div>
    <div class="nav-tile" style="background:var(--lime)"><svg viewBox="0 0 16 16"><circle cx="8" cy="5" r="3" fill="#fff"/><path d="M2 15c0-4 12-4 12 0z" fill="#fff"/></svg>Membership</div>
    <div class="nav-tile" style="background:var(--teal)"><svg viewBox="0 0 16 16"><path d="M2 8h12M8 2v12" stroke="#fff" stroke-width="1.4"/></svg>Peering</div>
    <div class="nav-tile" style="background:var(--magenta)"><svg viewBox="0 0 16 16"><rect x="3" y="2" width="10" height="12" fill="none" stroke="#fff" stroke-width="1.4"/></svg>News</div>
    <div class="nav-tile" style="background:var(--red)"><svg viewBox="0 0 16 16"><path d="M2 4h12v8H2zM2 4l6 5 6-5" fill="none" stroke="#fff" stroke-width="1.4"/></svg>Contact</div>
  </nav>
</header>

<section class="hero" role="img" aria-label="Photograph of network cables plugged into a switch">
  <div class="hero-arrow" style="left:0"><svg width="6" height="8"><path d="M5 0L1 4l4 4" stroke="#fff" fill="none"/></svg></div>
  <div class="hero-arrow" style="right:0"><svg width="6" height="8"><path d="M1 0l4 4-4 4" stroke="#fff" fill="none"/></svg></div>
  <h1 class="hero-title">Carrier neutral</h1>
  <p class="hero-text">Corvane Link is commercially neutral, carrier and ISP independent and is a not-for-profit organisation.</p>
</section>

<section class="intro">
  <h2>ACHIEVING GREATNESS TOGETHER</h2>
  <p>We are the country's only not-for-profit and independent internet peering provider. Member owned, carrier neutral, with proven high quality peering services since 1997.</p>
</section>

<section class="services">
  <h2>WHAT WE DO</h2>
  <div class="cards">
    <div class="card card-blue"><svg viewBox="0 0 20 20"><rect x="2" y="4" width="16" height="10" fill="none" stroke="#fff" stroke-width="1.5"/><path d="M7 17h6" stroke="#fff" stroke-width="1.5"/></svg><h3>MEMBER OWNED</h3><p>Run by our members, for members, with open governance and fair pricing for everyone.</p></div>
    <div class="card card-orange"><svg viewBox="0 0 20 20"><circle cx="10" cy="10" r="7" fill="none" stroke="#fff" stroke-width="1.5"/><circle cx="10" cy="10" r="2" fill="#fff"/></svg><h3>COMMERCIALLY NEUTRAL</h3><p>No carrier or provider gets preference, so every network peers on equal terms.</p></div>
    <div class="card card-yellow"><svg viewBox="0 0 20 20"><circle cx="10" cy="7" r="3.5" fill="#fff"/><path d="M3 18c0-6 14-6 14 0z" fill="#fff"/></svg><h3>AUSTRALIA WIDE</h3><p>Peering points in every major city, linking networks right across the nation today.</p></div>
  </div>
</section>

<section class="features">
  <div class="feature-photo" role="img" aria-label="Photograph of coloured network patch cables"></div>
  <ul class="feature-list">
    <li>Peering points across the nation</li>
    <li>Multilateral peering points</li>
    <li>Member owned &amp; driven</li>
    <li>Not-for-profit</li>
    <li>Strong membership base</li>
  </ul>
  <span class="btn-join">JOIN NOW</span>
</section>

<section class="partners">
  <h2>PEERING PARTNERS</h2>
  <div class="partner-row">
    <span class="partner">Norvella</span>
    <span class="partner">Brightfen</span>
    <span class="partner">Quillsoft</span>
    <span class="partner">Wavelane</span>
    <span class="partner">ostrander.example</span>
    <span class="partner">Yarrowby</span>
  </div>
</section>

<footer class="site-footer">
  <nav class="footer-nav"><span>Home</span><span>About</span><span>Membership</span><span>Peering</span><span>News</span><span>Contact</span></nav>
  <p class="footer-contact">PO Box 120, Perth WA 6000 · hello@corvanelink.example</p>
  <p class="footer-copy">© 2015 Corvane Link. All rights reserved.</p>
  <div class="footer-social">Follow us<div class="social-row"><span></span><span></span><span></span><span></span></div></div>
</footer>
</body>
</html>
```